Pop-up Banner

Would like a design for a pop-up 85 x 206cm banner for a trade show. (from norla press)
We would like "our logo" (brightwave holdings) - then the tagline - "Your Trusted Partner in Data-Driven Decisions"
*Supporting Bullets*
Unified data, analytics & AI
Trusted insights, faster outcomes
Real-time intelligence at scale
Enterprise-ready, secure solutions
Clarity from data complexity
trusted by...some company logos
Partners with : partner logo
Our Colours: #FFA300, #3D4176, #FDD16E, #F87C57, #A68118, #1C2F36

```html
<!DOCTYPE html>
<html lang="en">
<head>
<meta charset="utf-8">
<title>Brightwave Holdings – Pop-up Banner</title>
<link rel="stylesheet" href="https://fonts.googleapis.com/css2?family=Exo+2:ital,wght@0,700;1,700;1,800&family=Nunito:wght@400;600;700&display=swap">
<style>
  :root {
    --orange: #FFA300;
    --orange-deep: #F5A21F;
    --slate: #1C2F36;
    --slate-mid: #253a43;
    --navy: #3D4176;
    --sand: #FDD16E;
    --coral: #F87C57;
    --ochre: #A68118;
    --stage: #E39A1A;
    --ink: #1d2428;
    --white: #ffffff;
  }
  * { box-sizing: border-box; margin: 0; padding: 0; }
  html, body { width: 1200px; height: 800px; overflow: hidden; }
  body {
    background: var(--stage);
    font-family: "Exo 2", sans-serif;
    position: relative;
  }
  .banner {
    position: absolute;
    left: 439px;
    top: 20px;
    width: 322px;
    height: 760px;
    background: var(--slate);
    overflow: hidden;
  }
  .brand {
    position: absolute;
    top: 36px;
    left: 0;
    right: 0;
    display: flex;
    align-items: center;
    justify-content: center;
    gap: 12px;
  }
  .brand-mark {
    width: 50px; height: 50px;
    border-radius: 50%;
    border: 7px solid var(--orange);
  }
  .brand-name {
    color: var(--orange);
    font-weight: 700;
    font-size: 23px;
    line-height: 1.05;
    letter-spacing: 1px;
    text-transform: uppercase;
  }
  .tagline {
    position: absolute;
    top: 136px;
    left: 0; right: 0;
    text-align: center;
    color: var(--white);
    font-style: italic;
    font-weight: 700;
    font-size: 22.5px;
    line-height: 1.25;
  }
  .hero-photo {
    position: absolute;
    top: 200px;
    left: 0; right: 0;
    height: 285px;
    background:
      radial-gradient(ellipse at 50% 30%, #6fdcf0 0%, #2aa3c8 30%, transparent 65%),
      linear-gradient(180deg, var(--slate) 0%, #1f6a86 25%, #24506a 60%, var(--slate) 100%);
  }
  .benefits {
    position: absolute;
    top: 494px;
    left: 30px;
    right: 14px;
    list-style: none;
  }
  .benefits li {
    display: flex;
    align-items: center;
    gap: 11px;
    color: var(--orange);
    font-style: italic;
    font-weight: 800;
    font-size: 13.4px;
    height: 25.5px;
  }
  .benefits svg { width: 14px; height: 14px; flex: none; }
  .logo-band {
    position: absolute;
    top: 618px;
    left: 0; right: 0; bottom: 0;
    background: var(--orange-deep);
    font-family: "Nunito", sans-serif;
    text-align: center;
  }
  .band-label {
    color: var(--ink);
    font-weight: 600;
    font-size: 12px;
    margin-top: 8px;
  }
  .clients {
    display: grid;
    grid-template-columns: repeat(3, 1fr);
    row-gap: 6px;
    padding: 7px 18px 0;
  }
  .partners {
    display: grid;
    grid-template-columns: repeat(3, 1fr);
    padding: 5px 16px 0;
  }
  .org {
    display: flex;
    align-items: center;
    justify-content: center;
    gap: 4px;
    font-family: "Nunito", sans-serif;
    font-weight: 700;
    font-size: 14px;
    white-space: nowrap;
  }
  .org .dot { width: 9px; height: 9px; border-radius: 50%; }
  .org .sq { width: 9px; height: 9px; }
  .org--teal { color: #0f7d6f; }
  .org--blue { color: #3e8fd6; }
  .org--navy { color: var(--navy); }
  .org--dark { color: #2a2a2a; }
  .org--red { color: #c8283c; }
  .org--coral { color: var(--coral); }
  .org--green { color: #2e9a48; }
  .org--grey { color: #6b6b6b; }
  .partners .org { font-size: 11.5px; }
</style>
</head>
<body>
  <main class="banner">
    <header class="brand">
      <span class="brand-mark"></span>
      <span class="brand-name">Brightwave<br>Holdings</span>
    </header>

    <h1 class="tagline">Your Trusted Partner in<br>Data-Driven Decisions</h1>

    <div class="hero-photo" role="img" aria-label="Photo of a businessman wearing a VR headset standing in front of a glowing blue data dashboard wall, with colleagues around him"></div>

    <ul class="benefits">
      <li><svg viewBox="0 0 14 14"><rect x="1" y="2" width="11" height="11" fill="none" stroke="#FFA300" stroke-width="1.6"/><path d="M3.5 7.5l2.5 2.5 7-8" fill="none" stroke="#FFA300" stroke-width="1.8"/></svg>Unified data, analytics &amp; AI</li>
      <li><svg viewBox="0 0 14 14"><rect x="1" y="2" width="11" height="11" fill="none" stroke="#FFA300" stroke-width="1.6"/><path d="M3.5 7.5l2.5 2.5 7-8" fill="none" stroke="#FFA300" stroke-width="1.8"/></svg>Trusted insights, faster outcomes</li>
      <li><svg viewBox="0 0 14 14"><rect x="1" y="2" width="11" height="11" fill="none" stroke="#FFA300" stroke-width="1.6"/><path d="M3.5 7.5l2.5 2.5 7-8" fill="none" stroke="#FFA300" stroke-width="1.8"/></svg>Real-time intelligence at scale</li>
      <li><svg viewBox="0 0 14 14"><rect x="1" y="2" width="11" height="11" fill="none" stroke="#FFA300" stroke-width="1.6"/><path d="M3.5 7.5l2.5 2.5 7-8" fill="none" stroke="#FFA300" stroke-width="1.8"/></svg>Enterprise-ready, secure solutions</li>
      <li><svg viewBox="0 0 14 14"><rect x="1" y="2" width="11" height="11" fill="none" stroke="#FFA300" stroke-width="1.6"/><path d="M3.5 7.5l2.5 2.5 7-8" fill="none" stroke="#FFA300" stroke-width="1.8"/></svg>Clarity from data complexity</li>
    </ul>

    <section class="logo-band">
      <p class="band-label">Trusted By:</p>
      <div class="clients">
        <span class="org org--teal">Arcway</span>
        <span class="org org--blue">Quilltide</span>
        <span class="org org--navy"><span class="dot" style="background:#3e8fd6"></span>Marlow</span>
        <span class="org org--dark">Tallis</span>
        <span class="org org--red"><span class="sq" style="background:#c8283c"></span>Harbor Quay</span>
        <span class="org org--navy">Venturo</span>
      </div>
      <p class="band-label">Partners with:</p>
      <div class="partners">
        <span class="org org--coral">Corvane</span>
        <span class="org org--green"><span class="dot" style="background:#2e9a48"></span>clearmetric</span>
        <span class="org org--grey"><span class="sq" style="background:#6b6b6b"></span>Northpane</span>
      </div>
    </section>
  </main>
</body>
</html>
```